Document Proposal to be designed with Graphics and Professional looking

This is a letter to be sent to generate interest as a proposal for a Pharmaceutical Sale. The figure in the document are from different articles explaining the systems I will attach pictures. I am not sure if I want to use my official Logo, please feel free to place something appropriate for illustration purposes only

```html
<!DOCTYPE html>
<html lang="en">
<head>
<meta charset="utf-8">
<title>Buy and Bill System Proposal</title>
<link rel="stylesheet" href="https://fonts.googleapis.com/css2?family=Poppins:wght@300;400;600;700&display=swap">
<style>
:root{
  --teal:#0b8ea3;
  --teal-dark:#08788b;
  --sky:#3cb4d3;
  --sky-deep:#1f9cc0;
  --stage:#e6e6e9;
  --paper:#ffffff;
  --ink:#1c1c1c;
  --muted:#9a9ea3;
  --grey-band:#b2b4b8;
  --grey-strip:#d8d9dc;
}
*{box-sizing:border-box;margin:0;padding:0}
html,body{width:760px;height:1200px;overflow:hidden;background:var(--stage)}
body{position:relative;font-family:"Poppins",Arial,sans-serif;color:var(--ink)}
.page{position:absolute;width:257px;height:333px;background:var(--paper);overflow:hidden;box-shadow:0 1px 3px rgba(0,0,0,.18)}
.p1{left:108px;top:76px}.p2{left:395px;top:76px}
.p3{left:108px;top:444px}.p4{left:395px;top:444px}
.p5{left:108px;top:828px}.p6{left:395px;top:828px}
.shapes{position:absolute;left:0;top:0;width:257px;height:333px}
.footer{position:absolute;left:12px;top:323px;font-size:3.4px;letter-spacing:.05px;color:var(--muted);text-transform:uppercase}
.footer.light{color:#d6eef2}
.body-copy{font-size:4.3px;line-height:5.05px;font-weight:400}
.body-copy p{margin-bottom:5px}
.lead{font-weight:700;color:var(--teal);font-size:5.1px;line-height:6px}
.lead.white{color:#fff}

/* cover */
.cover-title{position:absolute;left:0;top:47px;width:166px;height:49px;background:var(--teal);border-radius:0 8px 8px 0;padding:9px 0 0 16px;color:#fff}
.cover-title h1{font-size:12.6px;font-weight:700;line-height:14px}
.cover-title .kicker{font-size:14.5px;font-weight:400;line-height:16px;letter-spacing:.2px}
.cover-intro{position:absolute;left:13px;top:224px;width:190px;font-size:6.3px;line-height:7.6px}
.cover-url{position:absolute;left:13px;top:261px;font-size:4.9px;font-weight:700;color:var(--teal)}

/* letter */
.letter{position:absolute;left:20px;top:22px;width:218px;color:#fff}
.letter h2{font-size:6.3px;font-weight:700;margin-bottom:7px}
.letter .lead{margin-bottom:8px}
.letter .body-copy p{margin-bottom:5px}

/* figures */
.figure{position:absolute;background:#fff;box-shadow:0 0 3px rgba(0,0,0,.22)}
.figure .art{width:100%;height:100%}

/* track & trace */
.tt-left{position:absolute;left:12px;top:140px;width:103px}
.tt-left .lead{margin-bottom:5px}
.tt-right{position:absolute;left:135px;top:141px;width:104px;color:#fff}

/* manufacturing */
.callout{position:absolute;left:0;top:99px;width:215px;height:52px;background:var(--teal);border-radius:0 8px 8px 0;padding:7px 0 0 12px}
.callout .lead{width:186px}
.mf-copy{position:absolute;left:12px;top:156px;width:178px}

/* production */
.band{position:absolute;left:0;top:89px;width:257px;height:88px;background:var(--teal)}
.prod-lead{position:absolute;left:15px;top:122px;width:214px}
.prod-copy{position:absolute;left:15px;top:182px;width:214px}

/* lims */
.lims-lead{position:absolute;left:12px;top:210px;width:142px}
</style>
</head>
<body>

<!-- Page 1: cover -->
<section class="page p1">
  <svg class="shapes" viewBox="0 0 257 333">
    <defs>
      <linearGradient id="pillTone" x1="0" y1="0" x2="1" y2="1">
        <stop offset="0" stop-color="#47bedb"/>
        <stop offset="1" stop-color="#2aa5c8"/>
      </linearGradient>
    </defs>
    <path d="M0 0 H257 V124 Q255 131 246 133 L0 190 Z" fill="url(#pillTone)" role="img" aria-label="Photo of white tablets scattered on a blue surface"/>
    <path d="M0 0 H48 Q34 36 0 38 Z" fill="var(--teal)"/>
    <path d="M0 325 L257 250 V333 H0 Z" fill="var(--teal)"/>
  </svg>
  <div class="cover-title">
    <h1>Buy and Bill system</h1>
    <div class="kicker">PROPOSAL</div>
  </div>
  <p class="cover-intro">Thank you for the opportunity to present our services and products. Please review some information about our process and distribution, as well as some examples of products we can provide you with.</p>
  <div class="cover-url">www.meridianrx-supply.com</div>
</section>

<!-- Page 2: letter -->
<section class="page p2">
  <svg class="shapes" viewBox="0 0 257 333">
    <path d="M7 0 H254 V308 L7 320 Z" fill="var(--teal)"/>
  </svg>
  <div class="letter">
    <h2>Dear Reader,</h2>
    <p class="lead white">Thank you for the opportunity to present our services and products. Please review some information about our process and distribution, as well as some examples of products we can provide you with.</p>
    <div class="body-copy">
      <p>We work with PDAB Accredited Drug Distributors to ensure strict standards and compliance processes; this ensures that licensure verifications, operational policies, and procedures, as well as proper and approved Drugs, are distributed. The Accreditation was put in place to ensure end buyers, which are Pharmacies that the drugs purchased are not counterfeit and are coming from the Brands and Manufacturers directly.</p>
      <p>In short, the PDAB Accreditation is important because it ensures the drugs you are paying for are genuine articles. With the rise of counterfeit drugs and wholesale distributors, PDAB created these rules to combat illegitimate wholesalers. That's also why we offer pedigree tracing for our drugs so you can rest assured the drugs you order are the ones your receive.</p>
      <p>We have access to most, if not all, FDA Brand name and Generic Equivalent medications. To give you some examples, please see some of the top medications which are currently distributed in United States Pharmacies, we have included them at the end of this document as Attachment A.</p>
      <p style="margin-bottom:0">Please provide us with a list of medications and quantities of the medication you are looking for; we will then reach out to our multiple warehouse distributors to find the best possible distributor to offer you as a possible option.</p>
      <p>Our Clinic uses what is referred to in the industry as a Buy and Bill system. In this flowchart below, we are the CLINIC = us; we work with multiple Rx Wholesalers, and in return, Rx Wholesalers work directly with Brands Manufacturers.</p>
    </div>
  </div>
  <div class="footer light">Buy and Bill system proposal | 02</div>
</section>

<!-- Page 3: track and trace -->
<section class="page p3">
  <svg class="shapes" viewBox="0 0 257 333">
    <path d="M126 135 L188 68 H257 V333 H195 L126 302 Z" fill="var(--teal)"/>
  </svg>
  <div class="figure" style="left:15px;top:17px;width:173px;height:101px">
    <svg class="art" viewBox="0 0 173 101" role="img" aria-label="Flowchart of distribution and reimbursement for provider-administered outpatient drugs under buy-and-bill">
      <rect width="173" height="101" fill="#f3f7fa"/>
    </svg>
  </div>
  <div class="tt-left">
    <p class="lead">Track and Trace is a method of following a product through the supply chain. In the pharmaceutical industry, this is often referred to as an e-pedigree.</p>
    <div class="body-copy">
      <p>Government mandates to serialize pharmaceutical products are increasing around the globe.</p>
      <p>E-pedigree or electronic pedigree is an electronic version of the drug pedigree document. As defined by the U.S Food and Drug Administration as part of the 2006 Compliance Policy Guide for the Prescription Drug Marketing Act - " A drug pedigree is a statement of origin that identifies each prior sale, purchase, or trade of a drug, including the date of those transactions and the names and addresses of all parties to them."</p>
    </div>
  </div>
  <div class="tt-right body-copy">
    <p>As a product moves from one place to the next, each company that handles the product must carry forward all of the previous e-pedigree information. When it reaches it's final destination, the retailer will have a complete document showing where that shipment has been and who has handled that shipment. This is done for many reasons. The primary reason is for safety, it helps protect consumers from contaminated medicine and counterfeit drugs. It also has benefits to the manufacturer. Having the ability to serialize down to the unit level can help cut costs associated with recalls, as well as being able to more efficiently manage their shipments.</p>
    <p>The first critical piece of the chain occurs right on the packaging line. Precise and consistent product handling, marking, inspection and data gathering are required to introduce accurate data into the front end of the system.</p>
    <p>Although pressure-sensitive labeling is the most common form of marking for bundles, cases and pallets, laser marking and ink jet coding are more common for units, because of space limitations and throughput speed requirements.</p>
  </div>
  <div class="footer">Buy and Bill system pro posal | 02</div>
</section>

<!-- Page 4: manufacturing -->
<section class="page p4">
  <svg class="shapes" viewBox="0 0 257 333">
    <defs>
      <linearGradient id="capsuleTone" x1="0" y1="0" x2="1" y2="1">
        <stop offset="0" stop-color="#c7c5bd"/>
        <stop offset=".5" stop-color="#a9c9d6"/>
        <stop offset="1" stop-color="#6fb3c9"/>
      </linearGradient>
    </defs>
    <path d="M0 0 H257 V150 L0 88 Z" fill="url(#capsuleTone)" role="img" aria-label="Close-up photo of blue tablets, white pills and amber capsules"/>
    <rect x="225" y="148" width="32" height="185" fill="var(--grey-strip)"/>
  </svg>
  <div class="callout">
    <p class="lead white">All manufacturing flows, whether making cars, pies, medical devices, or pharmaceuticals, take raw materials, and through a series of manufacturing processes, transform them into a final product. In pharmaceutical production the constituent parts include the active pharmaceutical ingredient (API), excipients, and packaging and labelling materials.</p>
  </div>
  <div class="mf-copy body-copy">
    <p>Pharmaceuticals in tablet form may have coating agents added to make them easier to swallow and coloring to differentiate them. Tablets are often packaged in blister packs of 20 or so with a cardboard carton on which key consumer information is printed. As with cars or ice-cream each constituent part from the API to the foil of the blister pack must be traceable back to the originating batch of each originating supplier. If multiple batches of the same material are used this must become part of the production record. The key is traceability; traceability of everything that went into the batch of a product.</p>
    <p>The GMP principles put forward by the US Food and Drug Administration help ensure the quality of manufactured products throughout the manufacturing, processing and packaging stages. They are used to create a quality framework for the manufacture of a wide variety of products, including drugs, medical devices, some food, and blood, to make sure that the products are safe, pure and effective. GMP principles address a wide range of issues as varied as recordkeeping, personnel qualifications, sanitation, cleanliness, equipment verification, process validation, and complaint handling, but offer individual manufacturers the flexibility to decide how to implement the necessary controls in the most appropriate way for their particular business.</p>
    <p>Per US FDA, Good Manufacturing Practice (cGMP) and FDA 21 CFR Part 11 in pharmaceutical companies is a key regulatory requirements. To meet these GMP requirements is extremely important. The failure of organizations to comply with GMP regulations in any context can result in very serious consequences. These include internal direct costs related to product failure, scrap, etc and remediation costs related to problem identification, correction and reporting. There could also be significant external costs such as regulatory action costs related to recalls, discontinuation, suspended operations, etc. There may be costs associated with loss of market share due to reduced product volume. There is also the cost associated with damage to the company's reputation, which can even affect share value.</p>
  </div>
  <div class="footer">Buy and Bill system pro posal | 02</div>
</section>

<!-- Page 5: tablet production -->
<section class="page p5">
  <div class="band"></div>
  <div class="figure" style="left:15px;top:21px;width:163px;height:91px">
    <svg class="art" viewBox="0 0 163 91" role="img" aria-label="Schematic of a tablet production line from API and excipient through mill, granulator, dryer, tablet press, coater and packaging">
      <rect width="163" height="91" fill="#eef2f9"/>
    </svg>
  </div>
  <p class="lead white prod-lead">An overview of a typical pharmaceutical tablet production line is shown in Figure 1. Like cooking, the exact proportions of the various raw ingredients are controlled by a recipe which defines the amount of API, and excipient required. The various ingredients may be milled and mixed to ensure an even distribution of API. Mixing can be performed as a slurry/wet mix which is dried and milled again to create a fine powder. This bulk powder may be mixed with further excipients before being formed into tablets in a tableting machine. The tablets may be coated and finally packaged as required.</p>
  <div class="prod-copy body-copy">
    <p>Testing will be performed at each critical stage of the flow from raw materials to the final packaged product. For example, the incoming raw materials may be re-tested to ensure they conform to the supplier's specification before being released for use. The output of the granulator may be tested to ensure the API is evenly mixed and the output from the milling checked to ensure the mixture still contains the correct proportions of API and is ground evenly. Samples of tablet from the final product are retained for dissolution, stability, and other quality assurance purposes.</p>
    <p>All LIMS require the ability to track samples and associated test results, create certificates of analysis (CofA), use barcoding and associate samples with key information such as batch and supplier. LIMS will also include the ability to manage calibration and maintenance of laboratory instruments, and records which instruments were used for each sample test, along with who tested that sample and whether they were competent to test it, and to control inventory of the chemicals and the laboratory consumables used in testing.</p>
    <p>But while a typical QC sampling flow monitors and reports on discreet samples, a manufacturing flow requires a broader range of information to be associated and combined for management and reporting. A manufacturing flow requires the addition of Recipe Management to control the raw materials and intermediate products going into each manufacturing batch; the ability to keep test results for each part of the flow (raw materials, intermediate stages and final product); to link test results to the originating raw materials/suppliers and final product/customers; the statistical tools to control the process within defined limits; and the ability to quickly retrieve and report on this data.</p>
  </div>
  <div class="footer">Buy and Bill system pro posal | 02</div>
</section>

<!-- Page 6: LIMS -->
<section class="page p6">
  <svg class="shapes" viewBox="0 0 257 333">
    <path d="M0 0 H257 V20 L0 52 Z" fill="var(--grey-band)"/>
  </svg>
  <div class="figure" style="left:12px;top:12px;width:197px;height:184px">
    <svg class="art" viewBox="0 0 197 184" role="img" aria-label="Laboratory information management workflow diagram from sample reception through analysis, quality control, verification and publication">
      <rect width="197" height="184" fill="#f2f6f7"/>
    </svg>
  </div>
  <p class="lead lims-lead">Laboratory information management systems (LIMS) are used extensively in laboratories in a huge number of industries to manage, track and report on samples, tests, test results and more. In manufacturing industries laboratory testing can be involved at every step, from raw material analysis through to the finished product</p>
  <div class="footer">Buy and Bill system pro posal | 02</div>
</section>

</body>
</html>
```